Adventure Business Cards

Please check out our website for style
Vertical card
Details:
Side 1
Logo
Business name: Kestrel Point Wildland Tours
Name: Colin Warbeck
Role: Director
Email: info@kestrelpointtours.com
Address: PO Box 71, Marlin Cove NSW 2471
Phone: +61 2 5550 1847
Web address: www.kestrelpointtours.com
Side 2
Taking pictures?
A Friendwall and Pixlane logo
Tag us in your pictures with
#kpwildtours
@kpwildtours
www.kestrelpointtours.com
Details:
Side 1
Logo
Name: Colin Warbeck
Role: Director
Phone: +61 2 5550 1847
Side 2
Taking pictures?
#kpwildtours
@kpwildtours

```html
<!DOCTYPE html>
<html lang="en">
<head>
<meta charset="utf-8">
<title>Kestrel Point Wildland Tours – Business Card</title>
<link rel="stylesheet" href="https://fonts.googleapis.com/css2?family=Open+Sans:wght@400;600;700&display=swap">
<style>
  :root {
    --backdrop: #c9c9c9;
    --paper: #ffffff;
    --brand-blue: #0f5aa8;
    --sky-blue: #bcd9f3;
    --ink: #1c2f4d;
    --sea-light: #8fc3e8;
    --sea-deep: #1d4f8f;
    --card-w: 441px;
    --card-h: 774px;
  }
  * { box-sizing: border-box; margin: 0; padding: 0; }
  html, body {
    width: 1059px; height: 1200px; overflow: hidden;
    background: var(--backdrop);
    font-family: "Open Sans", Arial, sans-serif;
  }
  .card {
    position: absolute;
    width: var(--card-w); height: var(--card-h);
    background: var(--paper);
    overflow: hidden;
    box-shadow: 0 2px 6px rgba(0,0,0,.25);
  }
  .card-front { left: 73px; top: 116px; }
  .card-back  { left: 558px; top: 239px; }
  .card-shapes { position: absolute; inset: 0; width: 100%; height: 100%; }

  .business-name {
    position: absolute; right: 28px; top: 78px;
    text-align: right; color: var(--brand-blue);
    font-size: 25px; line-height: 33px; font-weight: 400;
  }
  .name-band {
    position: absolute; left: 187px; right: 0; top: 189px; height: 67px;
    background: var(--brand-blue); color: var(--paper);
    padding: 10px 0 0 16px;
  }
  .person-name { font-size: 23px; line-height: 27px; letter-spacing: .5px; text-transform: uppercase; }
  .person-name strong { font-weight: 700; }
  .person-role { font-size: 13px; font-weight: 600; letter-spacing: .5px; }

  .logo-mark {
    position: absolute; left: 34px; top: 312px;
    width: 168px; height: 168px; border-radius: 50%;
    background: var(--brand-blue);
    display: flex; align-items: center; justify-content: center; text-align: center;
    color: var(--paper); font-size: 19px; font-weight: 700; line-height: 24px;
    padding: 20px;
  }

  .contact-list { position: absolute; right: 20px; top: 540px; list-style: none; }
  .contact-item {
    display: flex; justify-content: flex-end; align-items: center;
    color: var(--ink); font-size: 16px; line-height: 22px; text-align: right;
  }
  .contact-item svg { width: 22px; height: 22px; margin-left: 22px; flex: none; fill: var(--brand-blue); }
  .contact-address { margin-bottom: 16px; }
  .contact-email { margin-bottom: 22px; }
  .contact-web { margin-top: 70px; }

  .social-list { position: absolute; left: 0; top: 69px; list-style: none; }
  .social-item { display: flex; align-items: center; margin-bottom: 14px; }
  .social-square { width: 63px; height: 63px; background: var(--brand-blue); }
  .social-name { margin-left: 14px; color: var(--brand-blue); font-size: 20px; font-weight: 600; }

  .hashtag { font-family: "Open Sans", Arial, sans-serif; font-size: 27px; fill: var(--brand-blue); }
</style>
</head>
<body>

<section class="card card-front" aria-label="Card front">
  <svg class="card-shapes" viewBox="0 0 441 774" aria-hidden="true">
    <path d="M0,0 C30,210 120,390 270,425 C340,440 395,428 441,405 L441,774 L0,774 Z" fill="var(--sky-blue)"/>
    <path d="M170,432 C260,462 360,452 441,402 L441,452 C360,492 260,488 170,432 Z" fill="var(--brand-blue)"/>
  </svg>

  <h1 class="business-name">Kestrel Point<br>Wildland Tours</h1>

  <div class="name-band">
    <p class="person-name">Colin <strong>Warbeck</strong></p>
    <p class="person-role">DIRECTOR</p>
  </div>

  <div class="logo-mark">Kestrel Point Wildland Tours</div>

  <ul class="contact-list">
    <li class="contact-item contact-address">
      <span>PO Box 71,<br>Marlin Cove NSW 2471</span>
      <svg viewBox="0 0 24 24"><path d="M12 3 2 12h3v8h5v-6h4v6h5v-8h3z"/></svg>
    </li>
    <li class="contact-item contact-email">
      <span>info@kestrelpointtours.com</span>
      <svg viewBox="0 0 24 24"><path d="M2 5h20v14H2z M4 7v1l8 5 8-5V7l-8 5z" fill-rule="evenodd"/></svg>
    </li>
    <li class="contact-item contact-phone">
      <span>+61 2 5550 1847</span>
      <svg viewBox="0 0 24 24"><path d="M6.6 10.8a15 15 0 0 0 6.6 6.6l2.2-2.2c.3-.3.7-.4 1-.2 1.1.4 2.3.6 3.6.6.6 0 1 .4 1 1V20c0 .6-.4 1-1 1A17 17 0 0 1 3 4c0-.6.4-1 1-1h3.5c.6 0 1 .4 1 1 0 1.3.2 2.5.6 3.6.1.3 0 .7-.2 1z"/></svg>
    </li>
    <li class="contact-item contact-web">
      <span>www.kestrelpointtours.com</span>
      <svg viewBox="0 0 24 24"><path d="M12 2a10 10 0 1 0 0 20 10 10 0 0 0 0-20zm0 2c1 0 2.5 2.5 2.8 7H9.2C9.5 6.5 11 4 12 4zm-3 .6A12 12 0 0 0 7.2 11H4.1A8 8 0 0 1 9 4.6zm6 0a8 8 0 0 1 4.9 6.4h-3.1A12 12 0 0 0 15 4.6zM4.1 13h3.1a12 12 0 0 0 1.8 6.4A8 8 0 0 1 4.1 13zm5.1 0h5.6c-.3 4.5-1.8 7-2.8 7s-2.5-2.5-2.8-7zm7.6 0h3.1a8 8 0 0 1-4.9 6.4 12 12 0 0 0 1.8-6.4z"/></svg>
    </li>
  </ul>
</section>

<section class="card card-back" aria-label="Card back">
  <svg class="card-shapes" viewBox="0 0 441 774">
    <defs>
      <linearGradient id="sea-fill" x1="0" y1="0" x2="0" y2="1">
        <stop offset="0" stop-color="var(--sea-light)"/>
        <stop offset="0.35" stop-color="var(--sea-deep)"/>
        <stop offset="1" stop-color="#173a6a"/>
      </linearGradient>
      <path id="hashtag-arc" d="M20,262 C140,220 250,228 330,290"/>
    </defs>
    <path role="img" aria-label="Photo of two snorkellers smiling in the open sea"
          d="M0,318 C150,255 320,270 395,400 C440,480 445,640 430,774 L0,774 Z" fill="url(#sea-fill)"/>
    <path d="M0,318 C150,255 320,270 395,400 C440,480 445,640 430,774" fill="none" stroke="var(--brand-blue)" stroke-width="8"/>
    <text class="hashtag"><textPath href="#hashtag-arc">#kpwildtours</textPath></text>
  </svg>

  <ul class="social-list">
    <li class="social-item"><span class="social-square"></span><span class="social-name">Friendwall</span></li>
    <li class="social-item"><span class="social-square"></span><span class="social-name">Pixlane</span></li>
  </ul>
</section>

</body>
</html>
```